Consulting Group Website Landing Page Design

We are working with a Consulting Group in California. They provide consulting services to law enforcement agencies throughout the US.
Some sites to use for content:
https://www.marlowcrestcenter.org
https://www.jpellingroup.com
https://www.48rkventures.com
https://www.vdq.org
http://www.themirvalgroup.com
Thank you for taking the time to consider designing a website for us. We are web developers based in Stockton, CA, USA. Most of our projects go through the same process. Understanding this process may help you win a project with us. We custom-code all of our websites in-house. We don’t have any requirements as to what tools you use for your design, but we ask that you follow these guidelines. Plus, please send your designs in at least 1200px. wide so they do not pixelate when we show the client.
IMAGES:
If you use any images or icons in the design, we ask that you have a link to the asset so we can purchase the image/icon. Most of the designs we submit do not have the customer’s images on them unless they have some great images. Be creative; show us the feeling you are trying to portray with your image choices. Use any royalty-free site you choose. We subscribe to Velmora and mainly use their images, but we can purchase images outside of Velmora. PLEASE NOTE: we will not submit designs to clients with watermarks on the images.
FONTS:
We ask that you identify the fonts you’re using in the design. This can be done in a message if you want. We typically use Quintet Fonts and Velmora Fonts.
CONTENT:
We're always open to different content and ideas. We often submit designs with stock images so the client can see our vision. We typically take pictures after the website launch to use their images with our vision. Lorem Ipsum is fine for paragraphs, but we ask that you make the Headers with correct English. We want to be able to show the vision and identify the sections of the website.
INSPIRATION:
We typically add a couple of links in the brief of websites we like to help you get started in your design.
REVISIONS:
We do not often ask for revisions of the designs unless we see something in the design that may not appeal to the client. If there are slight changes that we want to make, we do that in the development process.
FEEDBACK:
We rarely give feedback on designs during the design process. We are working on many website projects and do not have the time to provide feedback. We usually respond if your request is well thought out and asks specific questions, but a note asking “feedback, please” usually goes unanswered.

```html
<!DOCTYPE html>
<html lang="en">
<head>
<meta charset="utf-8">
<title>Harborline Consulting</title>
<link href="https://fonts.googleapis.com/css2?family=DM+Serif+Display&family=Inter:ital,wght@0,400;0,500;0,600;0,700;1,400&family=Poppins:wght@600&display=swap" rel="stylesheet">
<style>
:root{
  --navy:#0a3d87;
  --green:#66a81c;
  --ink:#1d1d1f;
  --muted:#4a4a4a;
  --sky:#f2f7fe;
  --mist:#e8f1fd;
  --card-light:#d5e5fb;
  --white:#ffffff;
  --line:#cfcfcf;
}
*{margin:0;padding:0;box-sizing:border-box}
html,body{width:1200px;height:4165px;overflow:hidden}
body{position:relative;font-family:"Inter",sans-serif;color:var(--ink);background:var(--white)}
.abs{position:absolute}
.serif{font-family:"DM Serif Display",serif;font-weight:400}
.btn{position:absolute;display:flex;align-items:center;justify-content:center;background:var(--green);color:var(--white);font-size:12px;font-weight:700;border-radius:22px;height:43px}

/* header */
.header{left:0;top:0;width:1200px;height:95px;background:var(--white)}
.brand{display:flex;align-items:center;gap:10px;color:var(--navy);font-weight:700;font-size:26px;letter-spacing:.3px}
.brand .dot{width:44px;height:44px;border-radius:50%;background:var(--navy)}
.nav{top:37px;font-size:13px;font-weight:500;color:var(--ink)}
.nav.active{color:var(--green);font-weight:600}

/* hero */
.hero{left:0;top:95px;width:1200px;height:518px;background:var(--sky)}
.hero h1{left:125px;top:200px;font-size:67px;line-height:1;color:var(--ink)}
.hero-copy{left:125px;top:307px;width:700px;font-size:13px;line-height:25px;color:var(--ink)}

/* navy band */
.navy-band{left:0;top:613px;width:1200px;height:1150px;background:var(--navy)}
.who{left:125px;top:527px;width:475px;height:460px;background:var(--navy);box-shadow:0 10px 30px rgba(0,0,0,.25);color:var(--white)}
.who h2{position:absolute;left:63px;top:58px;font-size:48px}
.who p{position:absolute;left:63px;top:140px;width:340px;font-size:13px;line-height:23.3px}
.practice{left:600px;top:435px;width:475px;height:552px;background:var(--green);color:var(--white)}
.practice h2{position:absolute;right:52px;top:52px;font-size:41px;line-height:48px;text-align:right}
.practice p{position:absolute;left:50px;top:218px;width:380px;font-size:13px;line-height:23.3px;text-align:center}
.avatar{left:955px;top:953px;width:68px;height:68px;border-radius:50%;background:linear-gradient(#cfd6df,#5e6b7c);border:3px solid var(--white)}

.services-title{left:0;top:1082px;width:1200px;text-align:center;font-size:52px;line-height:58px;color:var(--white)}
.svc{top:1250px;width:320px;text-align:center;color:var(--white)}
.svc svg{display:block;margin:0 auto}
.svc h3{margin-top:36px;font-size:28px;font-family:"DM Serif Display",serif;font-weight:400}
.svc p{margin:14px auto 0;width:250px;font-size:13px;line-height:23.3px}

/* news */
.news-title{left:0;top:1855px;width:1200px;text-align:center;font-size:53px;color:var(--ink)}
.news-intro{left:220px;top:1940px;width:760px;text-align:center;font-size:13px;line-height:23.3px}
.photo{top:2037px;width:465px;height:455px}
.news-card{top:2535px;width:465px}
.news-card h3{font-family:"Poppins",sans-serif;font-weight:600;font-size:23px;color:var(--ink)}
.news-card p{margin-top:22px;font-size:13px;line-height:23.3px;color:var(--muted)}
.more{margin-top:38px;display:flex;align-items:center;gap:14px;color:var(--green);font-size:13px;font-weight:700}
.more span{display:block;width:52px;height:1px;background:var(--green)}

/* testimonials */
.testi{left:0;top:2875px;width:1200px;height:547px;background:var(--mist);overflow:hidden}
.testi h2{position:absolute;left:125px;top:142px;font-size:50px}
.testi .lead{position:absolute;left:125px;top:220px;width:290px;font-size:13.5px;line-height:25px}
.arrow{position:absolute;top:348px;width:50px;height:50px;border-radius:50%;background:var(--green);display:flex;align-items:center;justify-content:center}
.quote-card{position:absolute;top:100px;width:304px;height:348px;padding:40px 36px;text-align:center}
.quote-card .q{width:44px;height:44px;border-radius:50%;margin:0 auto 24px;display:flex;align-items:center;justify-content:center}
.quote-card p{font-size:12px;font-style:italic;line-height:25px}
.quote-card.dark{background:var(--navy);color:var(--white)}
.quote-card.dark .q{background:var(--white)}
.quote-card.light{background:var(--card-light);color:var(--muted)}
.quote-card.light .q{background:var(--navy)}

/* contact */
.contact h2{position:absolute;left:125px;top:3520px;font-size:45px}
.field{position:absolute;left:125px;width:405px;border:1px solid var(--line);font-size:11px;color:#8a8a8a;padding:0 28px;background:var(--white)}
.contact-note{left:125px;top:3960px;width:400px;font-size:11px;line-height:21px}
.foot-link{right:125px;font-size:13.5px;text-align:right}
.social{top:3943px;width:40px;height:40px;border-radius:50%;background:var(--green)}
.footer{left:0;top:4097px;width:1200px;height:68px;background:var(--navy);color:var(--white);font-size:13px;display:flex;align-items:center;justify-content:center}
</style>
</head>
<body>

<header class="abs header">
  <div class="abs brand" style="left:125px;top:25px"><span class="dot"></span>Harborline Consulting</div>
  <div class="abs nav active" style="left:588px">Home</div>
  <div class="abs nav" style="left:665px">Why Choose Us</div>
  <div class="abs nav" style="left:802px">Our Services</div>
  <div class="abs nav" style="left:922px">Clients</div>
  <div class="abs nav" style="left:1003px">Contact Us</div>
</header>

<section class="abs hero"></section>
<h1 class="abs serif hero h1" style="left:125px;top:205px;font-size:67px;line-height:1">Solutions For A Safer World</h1>
<p class="abs hero-copy">Lorem Ipsum is simply dummy text of the printing and typesetting industry. Lorem Ipsum has been the industry's standard dummy text ever since the 1500s,</p>
<div class="btn" style="left:125px;top:392px;width:205px">Get A Consultant</div>

<section class="abs navy-band"></section>

<article class="abs who">
  <h2 class="serif">Who We Are</h2>
  <p>Lorem Ipsum is simply dummy text of the printing and typesetting industry. Lorem Ipsum has been the industry's standard dummy text ever since the 1500s, when an unknown printer took a galley of type and scrambled it to make a type specimen book. It has survived not only five centuries, but also the leap into electronic typesetting, remaining essentially unchanged.</p>
  <div class="btn" style="left:63px;top:360px;width:175px">Read More</div>
</article>

<article class="abs practice">
  <h2 class="serif">Police And<br>Public Practices<br>Consulting Services</h2>
  <p>Lorem Ipsum is simply dummy text of the printing and typesetting industry. Lorem Ipsum has been the industry's standard dummy text ever since the 1500s, when an unknown printer took a galley of type and scrambled it to make a type specimen book. It has survived not only five centuries, but also the leap into electronic typesetting, remaining essentially unchanged. It was popularised in the 1960s with the release of Letraset sheets containing Lorem Ipsum passages, and more recently with desktop publishing software like Aldus PageMaker including versions of Lorem Ipsum.</p>
</article>
<div class="abs avatar" role="img" aria-label="Portrait photo of a consultant in a suit"></div>

<h2 class="abs serif services-title">Harborline Consulting<br>Services</h2>

<div class="abs svc" style="left:120px">
  <svg width="110" height="110" viewBox="0 0 110 110"><path d="M55 5 A50 50 0 1 1 5 55" fill="none" stroke="var(--green)" stroke-width="2"/><rect x="40" y="40" width="30" height="22" rx="2" fill="none" stroke="var(--green)" stroke-width="2"/><line x1="47" y1="68" x2="63" y2="68" stroke="var(--green)" stroke-width="2"/><circle cx="66" cy="62" r="6" fill="none" stroke="var(--green)" stroke-width="2"/></svg>
  <h3>Systems Assessment</h3>
  <p>Lorem Ipsum is simply dummy text of the printing and typesetting industry. Lorem Ipsum has been the industry's standard dummy text ever since the 1500s,</p>
</div>
<div class="abs svc" style="left:440px">
  <svg width="110" height="110" viewBox="0 0 110 110"><path d="M105 55 A50 50 0 1 1 55 5" fill="none" stroke="var(--green)" stroke-width="2"/><rect x="38" y="38" width="34" height="26" rx="2" fill="none" stroke="var(--green)" stroke-width="2"/><circle cx="55" cy="51" r="7" fill="none" stroke="var(--green)" stroke-width="2"/><line x1="60" y1="56" x2="66" y2="62" stroke="var(--green)" stroke-width="2"/></svg>
  <h3>Policy Analysis</h3>
  <p>Lorem Ipsum is simply dummy text of the printing and typesetting industry. Lorem Ipsum has been the industry's standard dummy text ever since the 1500s,</p>
</div>
<div class="abs svc" style="left:758px">
  <svg width="110" height="110" viewBox="0 0 110 110"><path d="M55 5 A50 50 0 1 1 5 55" fill="none" stroke="var(--green)" stroke-width="2"/><circle cx="55" cy="55" r="9" fill="none" stroke="var(--green)" stroke-width="2"/><path d="M55 38v8M55 64v8M38 55h8M64 55h8M43 43l5 5M62 62l5 5M67 43l-5 5M43 67l5-5" stroke="var(--green)" stroke-width="2"/></svg>
  <h3>Technology Solutions</h3>
  <p>Lorem Ipsum is simply dummy text of the printing and typesetting industry. Lorem Ipsum has been the industry's standard dummy text ever since the 1500s,</p>
</div>
<div class="btn" style="left:495px;top:1621px;width:210px">View All Services</div>

<h2 class="abs serif news-title">Latest News &amp; Services</h2>
<p class="abs news-intro">Lorem Ipsum is simply dummy text of the printing and typesetting industry. Lorem Ipsum has been the industry's standard dummy text ever since the 1500s,</p>

<div class="abs photo" style="left:125px;background:linear-gradient(135deg,#8a7a45,#2c3650 55%,#1a2233)" role="img" aria-label="Photo of two smiling police officers at an outdoor community event"></div>
<div class="abs photo" style="left:610px;background:linear-gradient(160deg,#b9bcc0,#6d7785 50%,#25324a)" role="img" aria-label="Photo of a traffic officer in a high-visibility vest speaking with a resident on a street"></div>

<article class="abs news-card" style="left:125px">
  <h3>Lorem Ipsum Is Simply Dummy Text</h3>
  <p>Lorem Ipsum is simply dummy text of the printing and typesetting industry. Lorem Ipsum has been the industry's standard dummy text ever since the 1500s, when an unknown printer took a galley of type and scrambled it to make a type specimen book. It has survived not only five centuries.</p>
  <div class="more">Read more<span></span></div>
</article>
<article class="abs news-card" style="left:610px">
  <h3>Lorem Ipsum Is Simply Dummy Text</h3>
  <p>Lorem Ipsum is simply dummy text of the printing and typesetting industry. Lorem Ipsum has been the industry's standard dummy text ever since the 1500s, when an unknown printer took a galley of type and scrambled it to make a type specimen book. It has survived not only five centuries.</p>
  <div class="more">Read more<span></span></div>
</article>

<section class="abs testi">
  <h2 class="serif">Testimonials</h2>
  <p class="lead">Lorem Ipsum is simply dummy text of the printing and typesetting industry. Lorem Ipsum has been the industry's standard dummy text ever since the 1500s,</p>
  <div class="arrow" style="left:125px"><svg width="14" height="14" viewBox="0 0 14 14"><path d="M9 2L4 7l5 5" fill="none" stroke="#fff" stroke-width="2.5"/></svg></div>
  <div class="arrow" style="left:188px"><svg width="14" height="14" viewBox="0 0 14 14"><path d="M5 2l5 5-5 5" fill="none" stroke="#fff" stroke-width="2.5"/></svg></div>
  <div class="quote-card dark" style="left:448px"><div class="q"><svg width="20" height="16" viewBox="0 0 20 16"><path d="M2 16V9q0-6 6-9l1 2q-3 2-3 5h3v9zM11 16V9q0-6 6-9l1 2q-3 2-3 5h3v9z" fill="var(--green)"/></svg></div><p>"Lorem Ipsum is simply dummy text of the printing and typesetting industry. Lorem Ipsum has been the industry's standard dummy text ever since the 1500s, when an unknown printer took a galley of type and scrambled it to make a type specimen book.</p></div>
  <div class="quote-card light" style="left:773px"><div class="q"><svg width="20" height="16" viewBox="0 0 20 16"><path d="M2 16V9q0-6 6-9l1 2q-3 2-3 5h3v9zM11 16V9q0-6 6-9l1 2q-3 2-3 5h3v9z" fill="var(--green)"/></svg></div><p>"Lorem Ipsum is simply dummy text of the printing and typesetting industry. Lorem Ipsum has been the industry's standard dummy text ever since the 1500s, when an unknown printer took a galley of type and scrambled it to make a type specimen book.</p></div>
  <div class="quote-card light" style="left:1097px"><div class="q"><svg width="20" height="16" viewBox="0 0 20 16"><path d="M2 16V9q0-6 6-9l1 2q-3 2-3 5h3v9zM11 16V9q0-6 6-9l1 2q-3 2-3 5h3v9z" fill="var(--green)"/></svg></div><p>"Lorem Ipsum is simply dummy text of the printing and typesetting industry. Lorem Ipsum has been the industry's standard dummy text ever since the 1500s, when an unknown printer took a galley of type and scrambled it to make a type specimen book.</p></div>
</section>

<section class="contact">
  <h2 class="serif">Get In Touch With Us</h2>
  <div class="field" style="top:3625px;height:46px;line-height:46px">Name</div>
  <div class="field" style="top:3685px;height:46px;line-height:46px">Email</div>
  <div class="field" style="top:3745px;height:170px;padding-top:14px">Message</div>
  <svg class="abs" style="left:488px;top:3880px" width="26" height="22" viewBox="0 0 26 22"><path d="M1 11L25 1 19 21 12 14z" fill="var(--green)"/><path d="M12 14L25 1" stroke="#fff" stroke-width="1.2"/></svg>
  <p class="abs contact-note">Lorem Ipsum is simply dummy text of the printing and typesetting industry. Lorem Ipsum has been the industry's standard</p>

  <div class="abs brand" style="left:773px;top:3540px"><span class="dot"></span>Harborline Consulting</div>
  <div class="abs foot-link" style="top:3667px">Home</div>
  <div class="abs foot-link" style="top:3717px">Why Choose Us</div>
  <div class="abs foot-link" style="top:3767px">Our Services</div>
  <div class="abs foot-link" style="top:3817px">Clients</div>
  <div class="abs foot-link" style="top:3867px">Contact Us</div>
  <div class="abs social" style="left:873px" aria-label="Social link"></div>
  <div class="abs social" style="left:927px" aria-label="Social link"></div>
  <div class="abs social" style="left:982px" aria-label="Social link"></div>
  <div class="abs social" style="left:1035px" aria-label="Social link"></div>
</section>

<footer class="abs footer">© 2023 by Harborline Consulting, Inc. All Rights Reserved</footer>

</body>
</html>
```